Fashion Design Business Card

I need a new business card designed for a new fashion company. I have attached what I have currently designed. I want it more feminine looking, the logo needs to be gold. I want it simple, feminine and stylish. Please give me some different ideas with the fonts.
Updates

I need to send the design we currently have, as we have worked out the logo.
You also need all of our details
Industry/Entity Type
Fashion
Look and feel
Each slider illustrates characteristics of the customer's brand and the style your logo design should communicate.

```html
<!DOCTYPE html>
<html lang="en">
<head>
<meta charset="utf-8">
<title>Lena Marchetti – Business Card Concepts</title>
<link rel="stylesheet" href="https://fonts.googleapis.com/css2?family=Open+Sans:wght@400;600;700&family=Crimson+Text:wght@400;700&family=Arimo:wght@400&display=swap">
<style>
  :root {
    --page: #ffffff;
    --board: #ececec;
    --label: #555555;
    --frame-line: #c9c9c9;
    --card-line: #d4d4d4;
    --ink: #111111;
    --accent-orange: #e8683a;
    --accent-red: #e8262a;
    --swoosh: #f07c22;
    --amber: #fbb41a;
    --amber-light: #fcd587;
    --sun: #fccf0e;
    --sun-deep: #fbb514;
    --gold: #f5c400;
    --white: #ffffff;
  }
  html, body {
    margin: 0;
    width: 1200px;
    height: 1172px;
    overflow: hidden;
    background: var(--page);
  }
  .board {
    position: absolute;
    left: 21px; top: 23px;
    width: 1157px; height: 1128px;
    background: var(--board);
    box-shadow: 0 1px 4px rgba(0,0,0,0.25);
  }
  .group-title, .side-label {
    position: absolute;
    margin: 0;
    font-family: "Arimo", Arial, sans-serif;
    font-weight: 400;
    color: var(--label);
    line-height: 1;
  }
  .group-title { font-size: 37px; }
  .side-label { font-size: 24px; }
  .card-frame {
    position: absolute;
    width: 556px; height: 358px;
    background: var(--white);
    border: 2px solid var(--frame-line);
    box-sizing: border-box;
    box-shadow: 0 2px 4px rgba(0,0,0,0.25);
  }
  .card {
    position: absolute;
    display: block;
  }
  .card--outlined { outline: 1px solid var(--card-line); }
  .name { font-family: "Open Sans", Arial, sans-serif; fill: var(--ink); letter-spacing: 0.5px; }
  .name--bold { font-weight: 700; }
  .tagline { font-family: "Crimson Text", Georgia, serif; }
  .phone { font-family: "Crimson Text", Georgia, serif; fill: var(--ink); }
  .contact { font-family: "Open Sans", Arial, sans-serif; fill: var(--ink); }
  .brand-mark { font-family: "Open Sans", Arial, sans-serif; font-weight: 600; fill: var(--gold); }
</style>
</head>
<body>
<main class="board" aria-label="Business card concepts">

  <h2 class="group-title" style="left:23px; top:23px;">Group -1</h2>
  <p class="side-label" style="left:23px; top:93px;">Front</p>
  <p class="side-label" style="left:590px; top:93px;">back</p>

  <!-- Concept one: front -->
  <div class="card-frame" style="left:15px; top:129px;"></div>
  <svg class="card card--outlined" style="left:26px; top:141px;" width="536" height="335" viewBox="0 0 457 286">
    <rect width="457" height="286" fill="var(--white)"/>
    <path d="M0,286 L0,272 C40,170 100,118 165,120 C235,124 285,205 350,220 C400,228 440,195 457,140 L457,286 Z" fill="var(--amber-light)"/>
    <path d="M0,286 L0,282 C40,180 100,128 165,130 C235,134 285,215 350,230 C400,238 440,205 457,152 L457,286 Z" fill="var(--amber)"/>
    <path d="M295,172 C330,210 370,225 400,215 C430,205 450,170 457,88 L457,120 C445,195 420,222 395,224 C360,227 320,208 295,172 Z" fill="var(--swoosh)"/>
    <text class="brand-mark" x="44" y="72" font-size="36">LM</text>
    <circle cx="112" cy="60" r="7" fill="var(--gold)"/>
    <text class="name" x="415" y="82" font-size="25" text-anchor="end">LENA MARCHETTI</text>
    <text class="tagline" x="413" y="104" font-size="18" text-anchor="end" fill="var(--accent-orange)">fashion design</text>
    <text class="phone" x="62" y="218" font-size="22">Ph. 0400312746</text>
    <text class="contact" x="62" y="234" font-size="12">Email:  lena@lenamarchetti.com</text>
    <text class="contact" x="62" y="255" font-size="12">Web:  www.lenamarchetti.com</text>
  </svg>

  <!-- Concept one: back -->
  <div class="card-frame" style="left:584px; top:129px;"></div>
  <svg class="card card--outlined" style="left:593px; top:141px;" width="535" height="335" viewBox="0 0 456 286">
    <rect width="456" height="286" fill="var(--white)"/>
    <path d="M0,30 C35,140 120,235 385,286 L0,286 Z" fill="var(--amber-light)"/>
    <path d="M0,44 C35,150 115,240 370,286 L0,286 Z" fill="var(--amber)"/>
    <text class="name" x="259" y="148" font-size="25" text-anchor="middle">LENA MARCHETTI</text>
    <text class="tagline" x="381" y="172" font-size="18" text-anchor="end" fill="var(--accent-orange)">fashion design</text>
  </svg>

  <h2 class="group-title" style="left:23px; top:545px;">Group -2</h2>
  <p class="side-label" style="left:23px; top:604px;">Front</p>
  <p class="side-label" style="left:590px; top:604px;">back</p>

  <!-- Concept two: front -->
  <div class="card-frame" style="left:15px; top:637px;"></div>
  <svg class="card" style="left:26px; top:648px;" width="533" height="334" viewBox="0 0 455 285">
    <rect width="455" height="285" fill="var(--sun)"/>
    <path d="M0,0 L190,0 C170,80 100,130 0,145 Z" fill="var(--white)"/>
    <path d="M0,145 C100,130 170,80 190,0 L202,0 C186,110 100,170 0,195 Z" fill="var(--sun-deep)"/>
    <rect y="258" width="455" height="27" fill="var(--sun-deep)"/>
    <text class="brand-mark" x="44" y="64" font-size="36">LM</text>
    <circle cx="112" cy="52" r="7" fill="var(--gold)"/>
    <text class="name name--bold" x="447" y="67" font-size="25" text-anchor="end">LENA MARCHETTI</text>
    <text class="tagline" x="323" y="89" font-size="21" font-weight="700" text-anchor="middle" fill="var(--accent-red)">Fashion design</text>
    <text class="phone" x="27" y="233" font-size="22">Ph. 0400312746</text>
    <text class="contact" x="27" y="253" font-size="12">Email:  lena@lenamarchetti.com</text>
    <text class="contact" x="27" y="274" font-size="12">Web:  www.lenamarchetti.com</text>
  </svg>

  <!-- Concept two: back -->
  <div class="card-frame" style="left:584px; top:637px;"></div>
  <svg class="card" style="left:593px; top:648px;" width="535" height="334" viewBox="0 0 456 285">
    <rect width="456" height="285" fill="var(--sun)"/>
    <rect y="258" width="456" height="27" fill="var(--sun-deep)"/>
    <text class="name name--bold" x="269" y="139" font-size="25" text-anchor="middle">LENA MARCHETTI</text>
    <text class="tagline" x="269" y="167" font-size="22" text-anchor="middle" fill="var(--accent-red)">Fashion design</text>
  </svg>

</main>
</body>
</html>
```